Long Established Local Fencing (not swords) Business needs fresh Business Cards

We need fresh double sided business cards for our Fencing Construction business, we are looking for something with our new logo design added, and maybe a photo background ?
We recently had cards made from Cardlyne and we were horrified with what we got back, the quality was terrible, so am looking for high quality format for good printing company to make.
We install Steelmora, Timber paling, Aluminium Slat Screening, Picket (timber and aluminium) and most other fencing installations.
Our website is brankelrails.com.au should you like to learn a bit more.
We do have logo in other formats if required.
We have been in business for over 35 years and we have used this as a "motto" it is on our signage

Industry/Entity Type

Construction

Contact Information for Business Card

Open to ideas, we need 3 x different cards, one generic with no name and 2 x others each with 1 of our bosses name on each, I will put into upload files.

Colors
ec1f27
000000
606060
f5f5f5

Requirements
Must have
• Company Name and Logo
• Address
• Contact details, phone, website, email etc
• Small space to write notes when leaving card at residence
Nice to have
• Our motto "Servicing the Peninsula for over 35 years"

```html
<!DOCTYPE html>
<html lang="en">
<head>
<meta charset="utf-8">
<title>Brankel Rails – Business Card</title>
<link rel="stylesheet" href="https://fonts.googleapis.com/css2?family=Montserrat:wght@700;800&family=Questrial&display=swap">
<style>
  :root {
    --brand-red: #dc3030;
    --brand-black: #000000;
    --brand-grey: #5c6466;
    --paper: #ffffff;
    --stage: #4d5259;
  }
  html, body {
    margin: 0;
    padding: 0;
    width: 1200px;
    height: 1200px;
    overflow: hidden;
    background: var(--stage);
  }
  .sheet {
    width: 1200px;
    height: 1200px;
    display: flex;
    flex-direction: column;
    align-items: center;
    justify-content: center;
    gap: 40px;
  }
  .card {
    display: block;
    width: 900px;
    height: 550px;
    box-shadow: 0 8px 24px rgba(0,0,0,0.35);
  }
  .fill-red { fill: var(--brand-red); }
  .fill-black { fill: var(--brand-black); }
  .fill-grey { fill: var(--brand-grey); }
  .fill-paper { fill: var(--paper); }
  .brand-name {
    font-family: "Montserrat", sans-serif;
    font-weight: 800;
    letter-spacing: 1px;
  }
  .person-name {
    font-family: "Montserrat", sans-serif;
    font-weight: 700;
    font-size: 40px;
    fill: var(--brand-red);
  }
  .detail {
    font-family: "Questrial", sans-serif;
    font-size: 23px;
    fill: var(--paper);
  }
  .detail-label {
    font-family: "Montserrat", sans-serif;
    font-weight: 700;
    fill: var(--brand-red);
  }
  .web-address {
    font-family: "Questrial", sans-serif;
    font-size: 30px;
    letter-spacing: 5px;
    fill: var(--paper);
  }
</style>
</head>
<body>
<main class="sheet">

  <!-- Front: contact side -->
  <svg class="card card-front" viewBox="0 0 900 550" xmlns="http://www.w3.org/2000/svg">
    <rect class="fill-paper" width="900" height="550"/>
    <polygon class="fill-red" points="390,0 470,0 330,190 520,460 190,460"/>
    <polygon class="fill-paper" points="300,460 450,360 520,460"/>
    <polygon class="fill-black" points="470,0 900,0 900,550 770,550 720,460 520,460 330,190"/>
    <polygon class="fill-grey" points="0,460 720,460 770,550 0,550"/>

    <g class="brand-lockup">
      <circle class="fill-red" cx="140" cy="90" r="34"/>
      <text class="brand-name" x="40" y="190" font-size="40" fill="#000">BRANKEL</text>
      <text class="brand-name" x="40" y="238" font-size="40" fill="#000">RAILS</text>
    </g>

    <g class="contact-block" text-anchor="end">
      <text class="person-name" x="860" y="115">DALE MORROW</text>
      <text class="detail" x="860" y="150">License No. 51627c</text>
      <rect class="fill-red" x="430" y="185" width="470" height="3"/>
      <text class="detail" x="880" y="240">PO Box 218 Marlow Bay NSW 2260</text>
      <text class="detail" x="880" y="280">(02) 43550182 : <tspan class="detail-label">P</tspan></text>
      <text class="detail" x="880" y="318">0400 555 271 : <tspan class="detail-label">M</tspan></text>
      <text class="detail" x="880" y="356">brankelrails@mailnest.com : <tspan class="detail-label">E</tspan></text>
    </g>

    <text class="web-address" x="100" y="517">www.brankelrails.com.au</text>
  </svg>

  <!-- Back: brand side -->
  <svg class="card card-back" viewBox="0 0 900 550" xmlns="http://www.w3.org/2000/svg">
    <rect class="fill-red" width="900" height="550"/>
    <g class="brand-lockup" text-anchor="middle">
      <circle class="fill-black" cx="450" cy="200" r="40"/>
      <text class="brand-name" x="450" y="310" font-size="52" fill="#000">BRANKEL</text>
      <text class="brand-name" x="450" y="370" font-size="52" fill="#000">RAILS</text>
    </g>
  </svg>

</main>
</body>
</html>
```